Web Design Project for tidewater tipoff

I love sports and I love Tidewater Tipoff. Every year, I run the office bracket pool. Being unhappy with the existing tidewater tipoff websites out there, I created my own bracket website last year. This year, I am looking to add more features and have a more polished design. I am a backend programmer so my design skills are poor.

Requirements
Must have
• Here is a list of all the features that are needed.

- A single elimination tournament bracket which initially contains 64 teams, with games of 2 teams each, 1 loser and 1 winner: who will move to the next game in the tournament to face another winning team.
- A list of badges earned by the participant and their friends.
- A list of upcoming games which will the following: the teams playing in the game, the friends rooting for the teams in the game, a message to the user if this game is an upset (differentiate between the user correctly picking the upset and the user not correctly picking the upset), a message to the user if this is a critical game in their bracket.

(I understand this is confusing and will attach a screenshot of my rough design ideas for the site)

Nice to have
• A super simple logo which will just be the name of the site in a decent font.

```html
<!DOCTYPE html>
<html lang="en">
<head>
<meta charset="utf-8">
<title>Better Bracket Pool</title>
<link href="https://fonts.googleapis.com/css2?family=Righteous&family=PT+Sans:wght@400;700&display=swap" rel="stylesheet">
<style>
:root{
  --page:#e9e9e9;
  --ink:#1d1d1d;
  --box-top:#fbfbfb;
  --box-bottom:#dcdcdc;
  --box-edge:#c4c4c4;
  --muted:#8a8a8a;
  --dark:#2b2b2b;
  --dark-2:#3b3b3b;
  --blue:#1f86e0;
  --red:#d62024;
  --cyan:#2cb5d8;
  --winner:#2a5fd6;
}
*{box-sizing:border-box;margin:0;padding:0}
html,body{width:929px;height:1200px;overflow:hidden;background:var(--page)}
body{font-family:"PT Sans",sans-serif;color:var(--ink)}
.stage{position:relative;width:991px;height:1280px;transform:scale(.9375);transform-origin:0 0;
  background:linear-gradient(#f1f1f1,#e2e2e2)}
.site-title{position:absolute;left:8px;top:14px;font-family:"Righteous",sans-serif;font-size:74px;
  letter-spacing:-1px;color:#1a1a1a;text-shadow:2px 3px 3px rgba(0,0,0,.35)}
.game{position:absolute;width:70px;height:42px;padding:2px 3px;
  background:linear-gradient(var(--box-top),var(--box-bottom));border:1px solid var(--box-edge);
  box-shadow:0 1px 2px rgba(0,0,0,.2);font-size:10px;line-height:11px}
.team{display:flex;justify-content:space-between;white-space:nowrap}
.team b{font-weight:700}
.team i{font-style:normal;color:var(--muted);font-size:8px}
.vs{display:block;text-align:center;font-size:15px;line-height:14px;font-weight:700;color:#fff;
  -webkit-text-stroke:1px #333;letter-spacing:1px}
.final-team{position:absolute;left:335px;width:70px;height:44px;padding:6px 6px 0;
  background:linear-gradient(var(--box-top),var(--box-bottom));border:1px solid var(--box-edge);
  box-shadow:0 1px 2px rgba(0,0,0,.2);text-align:center;font-size:12px;line-height:13px}
.final-team small{display:block;font-size:8px;color:var(--muted)}
.final-team .winner{display:block;color:var(--winner);font-weight:700;font-size:14px;line-height:14px}
.final-vs{position:absolute;left:335px;top:530px;width:70px;text-align:center;font-size:24px;font-weight:700;
  color:#fff;-webkit-text-stroke:1.2px #333;letter-spacing:2px}
.badges{position:absolute;left:748px;top:119px;width:234px}
.panel-head{background:linear-gradient(#3a3a3a,#222);color:#fff;font-size:16px;font-weight:700;
  height:33px;line-height:33px;padding-left:9px}
.badge{position:relative;height:95px;border-bottom:1px solid #d2d2d2}
.avatar{position:absolute;left:1px;top:7px;width:56px;height:64px;border:1px solid #bbb;
  background:linear-gradient(#dfe3e6 0 35%,#b58d72 35% 50%,#2c2f36 50%)}
.score{position:absolute;left:23px;top:76px;font-size:11px}
.badge-by{position:absolute;left:65px;top:8px;font-size:11px}
.badge-name{position:absolute;left:65px;top:25px;display:flex;align-items:center;gap:6px;font-size:11px}
.badge-name .seal{width:28px;height:28px;border-radius:50%}
.badge-name.blue{color:var(--cyan)} .badge-name.blue .seal{background:var(--cyan)}
.badge-name.red{color:var(--red)} .badge-name.red .seal{background:var(--red)}
.badge-why{position:absolute;left:65px;top:63px;font-size:11px}
.upcoming-head{position:absolute;left:4px;top:996px;width:983px;height:36px;line-height:36px;text-align:center;
  background:linear-gradient(#3a3a3a,#222);color:#fff;font-size:16px;font-weight:700}
.match{position:absolute;top:1048px;width:236px;height:181px;border-radius:5px;overflow:hidden;
  background:linear-gradient(#3c3c3c,#1e1e1e);box-shadow:0 2px 4px rgba(0,0,0,.4)}
.match-time{height:30px;line-height:30px;text-align:center;color:#fff;font-size:14px;
  background:linear-gradient(#4a4a4a,#2e2e2e);border-bottom:1px solid #111}
.match-teams{display:flex;justify-content:space-between;padding:4px 16px 0;color:#888;font-size:14px;line-height:14px}
.match-teams span{text-align:center}
.match-teams small{display:block;color:#ddd;font-size:10px}
.fans{position:absolute;top:67px;width:63px;height:86px;border-radius:3px;
  background:repeating-linear-gradient(90deg,#2a2d34 0 19px,#e8e8e8 19px 21px),linear-gradient(#c9a58a,#2a2d34)}
.fans.left{left:13px}.fans.right{right:13px}
.match-vs{position:absolute;top:92px;left:0;right:0;text-align:center;color:#fff;font-size:26px}
.upset{position:absolute;bottom:0;left:0;right:0;height:24px;line-height:24px;text-align:center;color:#fff;font-size:16px}
.upset.blue{background:var(--blue)}.upset.red{background:var(--red)}
</style>
</head>
<body>
<div class="stage">
<h1 class="site-title">Better Bracket Pool</h1>

<!-- left bracket -->
<div class="game" style="left:10px;top:121px"><p class="team"><b>1. Harbor</b><i>56</i></p><span class="vs">V/S</span><p class="team"><b>15. Ridgeview</b><i>22</i></p></div>
<div class="game" style="left:10px;top:174px"><p class="team"><b>1. Harbor</b><i>56</i></p><span class="vs">V/S</span><p class="team"><b>15. Ridgeview</b><i>22</i></p></div>
<div class="game" style="left:10px;top:227px"><p class="team"><b>1. Harbor</b><i>56</i></p><span class="vs">V/S</span><p class="team"><b>15. Ridgeview</b><i>22</i></p></div>
<div class="game" style="left:10px;top:280px"><p class="team"><b>1. Harbor</b><i>56</i></p><span class="vs">V/S</span><p class="team"><b>15. Ridgeview</b><i>22</i></p></div>
<div class="game" style="left:10px;top:335px"><p class="team"><b>1. Harbor</b><i>56</i></p><span class="vs">V/S</span><p class="team"><b>15. Ridgeview</b><i>22</i></p></div>
<div class="game" style="left:10px;top:388px"><p class="team"><b>1. Harbor</b><i>56</i></p><span class="vs">V/S</span><p class="team"><b>15. Ridgeview</b><i>22</i></p></div>
<div class="game" style="left:10px;top:441px"><p class="team"><b>1. Harbor</b><i>56</i></p><span class="vs">V/S</span><p class="team"><b>15. Ridgeview</b><i>22</i></p></div>
<div class="game" style="left:10px;top:493px"><p class="team"><b>1. Harbor</b><i>56</i></p><span class="vs">V/S</span><p class="team"><b>15. Ridgeview</b><i>22</i></p></div>
<div class="game" style="left:10px;top:547px"><p class="team"><b>1. Harbor</b><i>56</i></p><span class="vs">V/S</span><p class="team"><b>15. Ridgeview</b><i>22</i></p></div>
<div class="game" style="left:10px;top:600px"><p class="team"><b>1. Harbor</b><i>56</i></p><span class="vs">V/S</span><p class="team"><b>15. Ridgeview</b><i>22</i></p></div>
<div class="game" style="left:10px;top:652px"><p class="team"><b>1. Harbor</b><i>56</i></p><span class="vs">V/S</span><p class="team"><b>15. Ridgeview</b><i>22</i></p></div>
<div class="game" style="left:10px;top:705px"><p class="team"><b>1. Harbor</b><i>56</i></p><span class="vs">V/S</span><p class="team"><b>15. Ridgeview</b><i>22</i></p></div>
<div class="game" style="left:10px;top:760px"><p class="team"><b>1. Harbor</b><i>56</i></p><span class="vs">V/S</span><p class="team"><b>15. Ridgeview</b><i>22</i></p></div>
<div class="game" style="left:10px;top:812px"><p class="team"><b>1. Harbor</b><i>56</i></p><span class="vs">V/S</span><p class="team"><b>15. Ridgeview</b><i>22</i></p></div>
<div class="game" style="left:10px;top:866px"><p class="team"><b>1. Harbor</b><i>56</i></p><span class="vs">V/S</span><p class="team"><b>15. Ridgeview</b><i>22</i></p></div>
<div class="game" style="left:10px;top:918px"><p class="team"><b>1. Harbor</b><i>56</i></p><span class="vs">V/S</span><p class="team"><b>15. Ridgeview</b><i>22</i></p></div>

<div class="game" style="left:87px;top:148px"><p class="team"><b>1. Harbor</b><i>56</i></p><span class="vs">V/S</span><p class="team"><b>15. Ridgeview</b><i>22</i></p></div>
<div class="game" style="left:87px;top:256px"><p class="team"><b>1. Harbor</b><i>56</i></p><span class="vs">V/S</span><p class="team"><b>15. Ridgeview</b><i>22</i></p></div>
<div class="game" style="left:87px;top:364px"><p class="team"><b>1. Harbor</b><i>56</i></p><span class="vs">V/S</span><p class="team"><b>15. Ridgeview</b><i>22</i></p></div>
<div class="game" style="left:87px;top:472px"><p class="team"><b>1. Harbor</b><i>56</i></p><span class="vs">V/S</span><p class="team"><b>15. Ridgeview</b><i>22</i></p></div>
<div class="game" style="left:87px;top:574px"><p class="team"><b>1. Harbor</b><i>56</i></p><span class="vs">V/S</span><p class="team"><b>15. Ridgeview</b><i>22</i></p></div>
<div class="game" style="left:87px;top:682px"><p class="team"><b>1. Harbor</b><i>56</i></p><span class="vs">V/S</span><p class="team"><b>15. Ridgeview</b><i>22</i></p></div>
<div class="game" style="left:87px;top:790px"><p class="team"><b>1. Harbor</b><i>56</i></p><span class="vs">V/S</span><p class="team"><b>15. Ridgeview</b><i>22</i></p></div>
<div class="game" style="left:87px;top:898px"><p class="team"><b>1. Harbor</b><i>56</i></p><span class="vs">V/S</span><p class="team"><b>15. Ridgeview</b><i>22</i></p></div>

<div class="game" style="left:141px;top:202px"><p class="team"><b>1. Harbor</b><i>56</i></p><span class="vs">V/S</span><p class="team"><b>15. Ridgeview</b><i>22</i></p></div>
<div class="game" style="left:141px;top:417px"><p class="team"><b>1. Harbor</b><i>56</i></p><span class="vs">V/S</span><p class="team"><b>15. Ridgeview</b><i>22</i></p></div>
<div class="game" style="left:141px;top:630px"><p class="team"><b>1. Harbor</b><i>56</i></p><span class="vs">V/S</span><p class="team"><b>15. Ridgeview</b><i>22</i></p></div>
<div class="game" style="left:141px;top:845px"><p class="team"><b>1. Harbor</b><i>56</i></p><span class="vs">V/S</span><p class="team"><b>15. Ridgeview</b><i>22</i></p></div>

<div class="game" style="left:206px;top:311px"><p class="team"><b>1. Harbor</b><i>56</i></p><span class="vs">V/S</span><p class="team"><b>15. Ridgeview</b><i>22</i></p></div>
<div class="game" style="left:206px;top:740px"><p class="team"><b>1. Harbor</b><i>56</i></p><span class="vs">V/S</span><p class="team"><b>15. Ridgeview</b><i>22</i></p></div>
<div class="game" style="left:236px;top:521px"><p class="team"><b>1. Harbor</b><i>56</i></p><span class="vs">V/S</span><p class="team"><b>15. Ridgeview</b><i>22</i></p></div>

<!-- final -->
<div class="final-team" style="top:481px">1. Harbor<small>56</small></div>
<div class="final-vs">V/S</div>
<div class="final-team" style="top:562px;padding-top:3px"><span class="winner">WINNER</span>15. Ridgeview<small>22</small></div>

<!-- right bracket -->
<div class="game" style="left:428px;top:522px"><p class="team"><b>1. Harbor</b><i>56</i></p><span class="vs">V/S</span><p class="team"><b>15. Ridgeview</b><i>22</i></p></div>
<div class="game" style="left:458px;top:311px"><p class="team"><b>1. Harbor</b><i>56</i></p><span class="vs">V/S</span><p class="team"><b>15. Ridgeview</b><i>22</i></p></div>
<div class="game" style="left:458px;top:740px"><p class="team"><b>1. Harbor</b><i>56</i></p><span class="vs">V/S</span><p class="team"><b>15. Ridgeview</b><i>22</i></p></div>

<div class="game" style="left:522px;top:202px"><p class="team"><b>1. Harbor</b><i>56</i></p><span class="vs">V/S</span><p class="team"><b>15. Ridgeview</b><i>22</i></p></div>
<div class="game" style="left:522px;top:417px"><p class="team"><b>1. Harbor</b><i>56</i></p><span class="vs">V/S</span><p class="team"><b>15. Ridgeview</b><i>22</i></p></div>
<div class="game" style="left:522px;top:630px"><p class="team"><b>1. Harbor</b><i>56</i></p><span class="vs">V/S</span><p class="team"><b>15. Ridgeview</b><i>22</i></p></div>
<div class="game" style="left:522px;top:845px"><p class="team"><b>1. Harbor</b><i>56</i></p><span class="vs">V/S</span><p class="team"><b>15. Ridgeview</b><i>22</i></p></div>

<div class="game" style="left:584px;top:148px"><p class="team"><b>1. Harbor</b><i>56</i></p><span class="vs">V/S</span><p class="team"><b>15. Ridgeview</b><i>22</i></p></div>
<div class="game" style="left:584px;top:256px"><p class="team"><b>1. Harbor</b><i>56</i></p><span class="vs">V/S</span><p class="team"><b>15. Ridgeview</b><i>22</i></p></div>
<div class="game" style="left:584px;top:364px"><p class="team"><b>1. Harbor</b><i>56</i></p><span class="vs">V/S</span><p class="team"><b>15. Ridgeview</b><i>22</i></p></div>
<div class="game" style="left:584px;top:472px"><p class="team"><b>1. Harbor</b><i>56</i></p><span class="vs">V/S</span><p class="team"><b>15. Ridgeview</b><i>22</i></p></div>
<div class="game" style="left:584px;top:574px"><p class="team"><b>1. Harbor</b><i>56</i></p><span class="vs">V/S</span><p class="team"><b>15. Ridgeview</b><i>22</i></p></div>
<div class="game" style="left:584px;top:682px"><p class="team"><b>1. Harbor</b><i>56</i></p><span class="vs">V/S</span><p class="team"><b>15. Ridgeview</b><i>22</i></p></div>
<div class="game" style="left:584px;top:790px"><p class="team"><b>1. Harbor</b><i>56</i></p><span class="vs">V/S</span><p class="team"><b>15. Ridgeview</b><i>22</i></p></div>
<div class="game" style="left:584px;top:898px"><p class="team"><b>1. Harbor</b><i>56</i></p><span class="vs">V/S</span><p class="team"><b>15. Ridgeview</b><i>22</i></p></div>

<div class="game" style="left:658px;top:121px"><p class="team"><b>1. Harbor</b><i>56</i></p><span class="vs">V/S</span><p class="team"><b>15. Ridgeview</b><i>22</i></p></div>
<div class="game" style="left:658px;top:174px"><p class="team"><b>1. Harbor</b><i>56</i></p><span class="vs">V/S</span><p class="team"><b>15. Ridgeview</b><i>22</i></p></div>
<div class="game" style="left:658px;top:227px"><p class="team"><b>1. Harbor</b><i>56</i></p><span class="vs">V/S</span><p class="team"><b>15. Ridgeview</b><i>22</i></p></div>
<div class="game" style="left:658px;top:280px"><p class="team"><b>1. Harbor</b><i>56</i></p><span class="vs">V/S</span><p class="team"><b>15. Ridgeview</b><i>22</i></p></div>
<div class="game" style="left:658px;top:335px"><p class="team"><b>1. Harbor</b><i>56</i></p><span class="vs">V/S</span><p class="team"><b>15. Ridgeview</b><i>22</i></p></div>
<div class="game" style="left:658px;top:388px"><p class="team"><b>1. Harbor</b><i>56</i></p><span class="vs">V/S</span><p class="team"><b>15. Ridgeview</b><i>22</i></p></div>
<div class="game" style="left:658px;top:441px"><p class="team"><b>1. Harbor</b><i>56</i></p><span class="vs">V/S</span><p class="team"><b>15. Ridgeview</b><i>22</i></p></div>
<div class="game" style="left:658px;top:493px"><p class="team"><b>1. Harbor</b><i>56</i></p><span class="vs">V/S</span><p class="team"><b>15. Ridgeview</b><i>22</i></p></div>
<div class="game" style="left:658px;top:547px"><p class="team"><b>1. Harbor</b><i>56</i></p><span class="vs">V/S</span><p class="team"><b>15. Ridgeview</b><i>22</i></p></div>
<div class="game" style="left:658px;top:600px"><p class="team"><b>1. Harbor</b><i>56</i></p><span class="vs">V/S</span><p class="team"><b>15. Ridgeview</b><i>22</i></p></div>
<div class="game" style="left:658px;top:652px"><p class="team"><b>1. Harbor</b><i>56</i></p><span class="vs">V/S</span><p class="team"><b>15. Ridgeview</b><i>22</i></p></div>
<div class="game" style="left:658px;top:705px"><p class="team"><b>1. Harbor</b><i>56</i></p><span class="vs">V/S</span><p class="team"><b>15. Ridgeview</b><i>22</i></p></div>
<div class="game" style="left:658px;top:760px"><p class="team"><b>1. Harbor</b><i>56</i></p><span class="vs">V/S</span><p class="team"><b>15. Ridgeview</b><i>22</i></p></div>
<div class="game" style="left:658px;top:812px"><p class="team"><b>1. Harbor</b><i>56</i></p><span class="vs">V/S</span><p class="team"><b>15. Ridgeview</b><i>22</i></p></div>
<div class="game" style="left:658px;top:866px"><p class="team"><b>1. Harbor</b><i>56</i></p><span class="vs">V/S</span><p class="team"><b>15. Ridgeview</b><i>22</i></p></div>
<div class="game" style="left:658px;top:918px"><p class="team"><b>1. Harbor</b><i>56</i></p><span class="vs">V/S</span><p class="team"><b>15. Ridgeview</b><i>22</i></p></div>

<!-- badges -->
<section class="badges">
  <div class="panel-head">Badges Awarded</div>
  <div class="badge"><div class="avatar" role="img" aria-label="Portrait photo of Jeff"></div><span class="score">45</span><p class="badge-by">Jeff received the badege :</p><p class="badge-name blue"><span class="seal"></span>Harborite for life</p><p class="badge-why">For Picking Harbor over Lakeland</p></div>
  <div class="badge"><div class="avatar" role="img" aria-label="Portrait photo of Jeff"></div><span class="score">45</span><p class="badge-by">Jeff received the badege :</p><p class="badge-name red"><span class="seal"></span>Harborite for life</p><p class="badge-why">For Picking Harbor over Lakeland</p></div>
  <div class="badge"><div class="avatar" role="img" aria-label="Portrait photo of Jeff"></div><span class="score">45</span><p class="badge-by">Jeff received the badege :</p><p class="badge-name blue"><span class="seal"></span>Harborite for life</p><p class="badge-why">For Picking Harbor over Lakeland</p></div>
  <div class="badge"><div class="avatar" role="img" aria-label="Portrait photo of Jeff"></div><span class="score">45</span><p class="badge-by">Jeff received the badege :</p><p class="badge-name red"><span class="seal"></span>Harborite for life</p><p class="badge-why">For Picking Harbor over Lakeland</p></div>
  <div class="badge"><div class="avatar" role="img" aria-label="Portrait photo of Jeff"></div><span class="score">45</span><p class="badge-by">Jeff received the badege :</p><p class="badge-name blue"><span class="seal"></span>Harborite for life</p><p class="badge-why">For Picking Harbor over Lakeland</p></div>
  <div class="badge"><div class="avatar" role="img" aria-label="Portrait photo of Jeff"></div><span class="score">45</span><p class="badge-by">Jeff received the badege :</p><p class="badge-name red"><span class="seal"></span>Harborite for life</p><p class="badge-why">For Picking Harbor over Lakeland</p></div>
  <div class="badge"><div class="avatar" role="img" aria-label="Portrait photo of Jeff"></div><span class="score">45</span><p class="badge-by">Jeff received the badege :</p><p class="badge-name blue"><span class="seal"></span>Harborite for life</p><p class="badge-why">For Picking Harbor over Lakeland</p></div>
  <div class="badge"><div class="avatar" role="img" aria-label="Portrait photo of Jeff"></div><span class="score">45</span><p class="badge-by">Jeff received the badege :</p><p class="badge-name red"><span class="seal"></span>Harborite for life</p><p class="badge-why">For Picking Harbor over Lakeland</p></div>
</section>

<!-- upcoming games -->
<div class="upcoming-head">Upcoming Games</div>
<div class="match" style="left:10px"><div class="match-time">Tuesday 1:05 PM (PST)</div><div class="match-teams"><span>1. Harbor<small>56</small></span><span>15. Ridgeview<small>22</small></span></div><div class="fans left" role="img" aria-label="Grid of friends rooting for Harbor"></div><div class="match-vs">V/S</div><div class="fans right" role="img" aria-label="Grid of friends rooting for Ridgeview"></div></div>
<div class="match" style="left:252px"><div class="match-time">Tuesday 1:05 PM (PST)</div><div class="match-teams"><span>1. Harbor<small>56</small></span><span>15. Ridgeview<small>22</small></span></div><div class="fans left" role="img" aria-label="Grid of friends rooting for Harbor"></div><div class="match-vs">V/S</div><div class="fans right" role="img" aria-label="Grid of friends rooting for Ridgeview"></div><div class="upset blue">Upset!</div></div>
<div class="match" style="left:494px"><div class="match-time">Tuesday 1:05 PM (PST)</div><div class="match-teams"><span>1. Harbor<small>56</small></span><span>15. Ridgeview<small>22</small></span></div><div class="fans left" role="img" aria-label="Grid of friends rooting for Harbor"></div><div class="match-vs">V/S</div><div class="fans right" role="img" aria-label="Grid of friends rooting for Ridgeview"></div><div class="upset red">Upset!</div></div>
<div class="match" style="left:734px"><div class="match-time">Tuesday 1:05 PM (PST)</div><div class="match-teams"><span>1. Harbor<small>56</small></span><span>15. Ridgeview<small>22</small></span></div><div class="fans left" role="img" aria-label="Grid of friends rooting for Harbor"></div><div class="match-vs">V/S</div><div class="fans right" role="img" aria-label="Grid of friends rooting for Ridgeview"></div></div>
</div>
</body>
</html>
```